New Alcoholic Spiked Seltzer Line

We need a can design for a line of low calorie alcoholic seltzer. This product is a sparkling water and vodka drink with no sugar added in a slim 12 oz can.

This is a lighter, healthier, alternative to the sugary ready-to-drinks on the market. The product contains only 3 ingredients: Vodka, Water and Natural Flavors. It has only 100 calories but still has 5% alcohol, so you don't need to sacrifice alcohol to cut calories.

This product also does not contain any preservatives.

We want this design to communicate the following objectives to the consumer and in this order:

1. Appetizing product
2.Low calorie
3.Communicate the type of beverage (Spiked Seltzer)

The brand name of the product is VELKA.

The flavor of the product needed to be used for the design is Mango-Orange.

Comparable products are:

www.brisavelfizz.example/
https://www.tarnowbubble.example
https://quellrind.example/

The designs should not infringe or copy the creative directions of the products mentionned above. They are only given so that you can better understand the type of product we are developing.

Target Market(s)

Young Professional women between the ages of 25 and 44

Industry/Entity Type

Product

Colors

Designer to choose colors to be used in the design.

Requirements
Must have
• Design extendibility, meaning it can be adapted for other flavors.
• This is a new category in the market we are targeting, so consumers must easily be able to identify what type of product this is.

```html
<!DOCTYPE html>
<html lang="en">
<head>
<meta charset="utf-8">
<title>VELKA Spiked Seltzer – Mango Can Label</title>
<link rel="stylesheet" href="https://fonts.googleapis.com/css2?family=Cinzel:wght@700&family=Yesteryear&family=Montserrat:wght@400;600&family=Oswald:wght@600&family=EB+Garamond:ital@0;1&display=swap">
<style>
  :root {
    --blue-deep: #145a84;
    --blue-mid: #1b7cab;
    --gold-deep: #c9911c;
    --gold-light: #f4d446;
    --label-white: #f1f1f1;
    --ink-grey: #6f6f6f;
    --script-blue: #1a6a9a;
    --page-bg: #ffffff;
  }
  * { box-sizing: border-box; margin: 0; padding: 0; }
  html, body { width: 722px; height: 1200px; overflow: hidden; background: var(--page-bg); }
  .label { position: relative; width: 722px; height: 1200px; background: var(--label-white); }
  .label-bands { position: absolute; inset: 0; }
  .eyebrow {
    position: absolute; top: 48px; width: 100%; text-align: center;
    font: 600 17px/1 "Montserrat", sans-serif; letter-spacing: 1.5px; color: #fff;
  }
  .brand {
    position: absolute; top: 400px; width: 100%; text-align: center;
    font: 700 112px/1 "Cinzel", serif; color: var(--gold-deep); letter-spacing: 2px;
  }
  .tagline-script {
    position: absolute; top: 520px; width: 100%; text-align: center;
    font: 48px/1 "Yesteryear", cursive; color: var(--script-blue);
  }
  .claims {
    position: absolute; top: 590px; width: 100%; text-align: center;
    font: 400 19px/1.4 "Montserrat", sans-serif; color: var(--ink-grey);
  }
  .flavour {
    position: absolute; top: 700px; width: 100%; text-align: center;
    font: 600 34px/1 "Oswald", sans-serif; letter-spacing: 2px; color: var(--gold-deep);
  }
  .fruit-badge {
    position: absolute; left: 236px; top: 770px; width: 250px; height: 250px;
    border-radius: 50%; border: 7px solid var(--blue-deep);
    background: radial-gradient(circle at 50% 55%, #f7c33a 0%, #f0a623 45%, #f3efe9 72%);
  }
  .benefits {
    position: absolute; top: 1088px; width: 100%; text-align: center;
    font: 400 27px/1 "EB Garamond", serif; color: #fff;
  }
  .spec {
    position: absolute; top: 1130px; color: #fff; text-align: center;
    font: italic 400 36px/1 "EB Garamond", serif;
  }
  .spec small { display: block; font-size: 26px; margin-top: 2px; }
  .spec-abv { left: 110px; }
  .spec-volume { right: 110px; }
</style>
</head>
<body>
<main class="label">
  <svg class="label-bands" width="722" height="1200" viewBox="0 0 722 1200" aria-hidden="true">
    <defs>
      <linearGradient id="blueBand" x1="0" x2="1" y1="0" y2="0">
        <stop offset="0" stop-color="var(--blue-deep)"/>
        <stop offset="0.5" stop-color="var(--blue-mid)"/>
        <stop offset="1" stop-color="var(--blue-deep)"/>
      </linearGradient>
      <linearGradient id="goldBand" x1="0" x2="1" y1="0" y2="0">
        <stop offset="0" stop-color="var(--gold-light)"/>
        <stop offset="0.5" stop-color="#e2ae22"/>
        <stop offset="1" stop-color="var(--gold-deep)"/>
      </linearGradient>
    </defs>
    <!-- top blue band with gold trim -->
    <path d="M0 0 H722 V252 Q361 150 0 252 Z" fill="url(#goldBand)"/>
    <path d="M0 0 H722 V232 Q361 132 0 232 Z" fill="url(#blueBand)"/>
    <!-- lower gold band -->
    <path d="M0 810 Q361 690 722 810 V990 Q361 1090 0 990 Z" fill="url(#goldBand)"/>
    <!-- bottom blue band -->
    <path d="M0 978 Q361 1080 722 978 V1200 H0 Z" fill="#0d4a3e"/>
    <path d="M0 990 Q361 1090 722 990 V1200 H0 Z" fill="url(#blueBand)"/>
  </svg>

  <p class="eyebrow">APPETIZING PRODUCT</p>
  <h1 class="brand">VELKA</h1>
  <p class="tagline-script">Lorum Ipsum</p>
  <p class="claims">Appetizing product Low calorie<br>Communicate the type of beverage<br>(Spiked Seltzer)</p>
  <p class="flavour">MANGO</p>
  <div class="fruit-badge" role="img" aria-label="Photo of ripe mangoes, one cut in a cubed hedgehog pattern"></div>
  <p class="benefits">Lighter - Healthier - Alternative</p>
  <p class="spec spec-abv">5.0%<small>All/ Vol</small></p>
  <p class="spec spec-volume">12.0<small>Fl /OZ</small></p>
</main>
</body>
</html>
```